New Website for ReBranded Company - CrewBeacon

We have a successful company and website currently but it is a little dated. We have re-branded the company from Harbor Signal Networks to CrewBeacon and have a new logo for the new name. We are looking to build a newer fresher website with the new name. I will need a concept of the home page and one inside page. You can see our current site at https://www.harborsignalnetworks.example and the new site will be https://www.crewbeacon.example .

I also really like the https://www.pathmolder.example/ website. I like ledgerleaf.example website. I like the https://skillbinder.example/ website.

See the attached document for layout and some text to use. Use the pictures I attached as opposed to pictures from the old site as much as you can.

Target Market(s)

Business

Industry/Entity Type

Software Service

Number of Pages Required

2 page

Font styles to use
Sans Serif

Requirements
Must have
• Use the colors from my logo. Professional but modern. We want people to feel like our product makes their staff feel safer at work.
Should not have
• Don't use any red or orange (no stop colors).

```html
<!DOCTYPE html>
<html lang="en">
<head>
<meta charset="utf-8">
<title>CrewBeacon — Get Help Fast</title>
<link rel="stylesheet" href="https://fonts.googleapis.com/css2?family=Poppins:wght@400;500;600;700;800&display=swap">
<style>
:root{
  --blue:#2f8fd8;
  --green:#7ab648;
  --navy:#143856;
  --navy-deep:#0f2d47;
  --teal:#1f5d63;
  --ink:#2a2a2a;
  --muted:#555;
  --light:#f7f7f7;
  --white:#fff;
  --photo:#9aa3aa;
}
*{box-sizing:border-box;margin:0;padding:0}
html,body{width:1200px;height:3750px;overflow:hidden}
body{font-family:"Poppins",sans-serif;color:var(--ink);background:var(--white);position:relative}
.abs{position:absolute}
.btn{position:absolute;display:flex;align-items:center;justify-content:center;background:var(--green);color:#fff;font-size:10.5px;font-weight:600;letter-spacing:.4px;text-transform:uppercase;text-decoration:none;white-space:nowrap}
.btn.blue{background:var(--blue)}
.photo{position:absolute}

/* header */
.site-header{position:absolute;left:0;top:0;width:1200px;height:68px;background:#fff}
.brand{position:absolute;display:flex;align-items:center;gap:8px;font-weight:600;color:var(--blue);white-space:nowrap}
.brand .dot{width:30px;height:30px;border-radius:50%;background:var(--blue)}
.nav a{position:absolute;font-size:11.5px;color:var(--blue);text-decoration:none;top:27px}
.nav .active{border-bottom:2px solid var(--blue);padding-bottom:16px}

/* hero */
.hero{position:absolute;left:0;top:68px;width:1200px;height:414px;background:linear-gradient(90deg,var(--teal),var(--navy) 70%)}
.hero h1{position:absolute;left:172px;top:105px;font-size:40px;line-height:43px;font-weight:800;color:#fff;text-transform:uppercase;white-space:nowrap}
.hero h1 span{color:var(--green)}
.hero p{position:absolute;left:172px;top:214px;font-size:14px;color:#fff}

.feature-box{position:absolute;left:172px;top:441px;width:271px;height:286px;background:var(--green);border-top:5px solid #fff;box-shadow:0 6px 14px rgba(0,0,0,.15);padding:28px 22px 0 21px;color:#fff;font-size:12.5px;line-height:19px}
.feature-box p{padding-bottom:14px}
.feature-box hr{border:0;border-top:1px solid rgba(255,255,255,.6);width:155px;margin:0 auto 16px}

.intro h2{position:absolute;left:539px;top:533px;font-size:32px;color:var(--blue);font-weight:700;text-transform:uppercase;white-space:nowrap}
.intro h3{position:absolute;left:539px;top:572px;font-size:22px;color:var(--green);font-weight:700;text-transform:uppercase;white-space:nowrap}
.intro p{position:absolute;left:539px;font-size:12px;color:var(--ink)}

/* why us */
.why{position:absolute;left:0;top:815px;width:1200px;height:1255px;background:var(--light)}
.section-title{position:absolute;left:0;width:1200px;text-align:center;font-size:30px;font-weight:700;color:var(--blue);text-transform:uppercase}
.underline{position:absolute;left:492px;width:216px;height:2px;background:var(--green)}
.underline::after{content:"";position:absolute;left:30px;right:30px;top:3px;height:1px;background:var(--blue)}
.icon-badge{position:absolute;width:44px;height:44px;border-radius:50%;display:flex;align-items:center;justify-content:center}
.feat-title{position:absolute;font-size:22px;font-weight:700;color:var(--blue);text-transform:uppercase;white-space:nowrap}
.feat-text{position:absolute;font-size:12px;line-height:20px;color:var(--ink)}
.channel{position:absolute;width:89px;height:73px;border:1px solid var(--green);background:#fff;display:flex;flex-direction:column;align-items:center;justify-content:flex-end;padding-bottom:6px;font-size:11px;color:#333;gap:6px}
.channel.on{background:var(--green);color:#fff}
.mock-card{position:absolute;left:684px;top:1372px;width:344px;height:233px;background:#fff;box-shadow:0 4px 16px rgba(0,0,0,.12)}
.mock-card .frame{position:absolute;left:14px;top:14px;right:14px;bottom:14px;border:2px dashed var(--blue);padding:8px}
.mock-card .art{width:100%;height:100%;background:linear-gradient(135deg,#eef4e8,#e3eef8)}

/* reach */
.reach{position:absolute;left:0;top:2070px;width:1200px;height:303px;background:linear-gradient(90deg,var(--teal),var(--navy))}
.stat-card{position:absolute;left:172px;top:2137px;width:416px;height:171px;background:#fff;border-radius:4px}
.stat-card p{position:absolute;left:0;width:416px;top:22px;text-align:center;font-size:13px;line-height:20px}
.stat{position:absolute;top:96px;font-size:16px;font-weight:600}
.stat small{display:block;font-size:10px;font-weight:500;margin-top:6px;letter-spacing:.3px}
.quote-box{position:absolute;left:734px;top:2213px;width:293px;height:111px;background:rgba(26,60,97,.9);color:#fff;padding:26px 20px 0 40px;font-size:12px;line-height:19px}
.quote-box .mark{position:absolute;left:12px;top:12px;font-size:34px;font-weight:700;line-height:1}
.quote-box b{display:block;font-size:10px;margin-top:14px}
.demo-play{position:absolute;left:1070px;top:2222px;width:84px;height:84px;border-radius:50%;background:var(--green);box-shadow:0 0 0 7px rgba(122,182,72,.35);color:#fff;font-size:10px;font-weight:600;text-align:center;line-height:11px;padding-top:20px}

/* plan */
.step{position:absolute;width:271px;background:var(--navy);color:#fff;text-align:center;overflow:visible}
.step svg.cap{position:absolute;left:0;top:0}
.step .num{position:absolute;left:103px;top:-30px;width:64px;height:64px;border-radius:50%;border:4px solid #fff;color:#fff;font-size:28px;font-weight:700;display:flex;align-items:center;justify-content:center}
.step h4{position:absolute;left:0;width:271px;font-size:15px;font-weight:700;text-transform:uppercase;line-height:20px}
.step ul{list-style:none;position:absolute;left:65px;width:141px;font-size:12.5px}
.step li{height:32px;line-height:32px;border-bottom:1px solid rgba(255,255,255,.55);white-space:nowrap}
.step li:last-child{border-bottom:0}

/* crisis */
.crisis h2{position:absolute;left:0;width:1200px;text-align:center;font-size:31px;font-weight:700;color:#fff;text-transform:uppercase}
.crisis h3{position:absolute;left:0;width:1200px;text-align:center;font-size:24px;font-weight:700;color:var(--green);text-transform:uppercase}

/* footer */
.footer-col h5{position:absolute;top:3452px;font-size:14px;font-weight:600;color:#fff;text-transform:uppercase;display:flex;align-items:center;gap:8px}
.footer-col h5::after{content:"";width:48px;height:1px;background:var(--green)}
.footer-col ul{list-style:none;position:absolute;top:3497px;font-size:12.5px;color:#fff}
.footer-col li{height:27px;white-space:nowrap}
.footer-col li::before{content:"» ";color:var(--green)}
.call-box{position:absolute;left:794px;top:3359px;width:234px;height:48px;background:var(--blue);color:#fff;font-size:13px;font-weight:600;display:flex;align-items:center;justify-content:center;gap:10px}
</style>
</head>
<body>

<header class="site-header">
  <div class="brand" style="left:172px;top:17px;font-size:21px"><span class="dot"></span>CrewBeacon</div>
  <nav class="nav">
    <a class="active" href="#" style="left:574px">HOME</a>
    <a href="#" style="left:640px">BUY ADDONS</a>
  </nav>
  <a class="btn" href="#" style="left:748px;top:19px;width:104px;height:31px;font-size:9.5px">&#9679;&nbsp;Cust Login</a>
  <a class="btn blue" href="#" style="left:869px;top:19px;width:155px;height:31px;font-size:9.5px">Explore Your Choices</a>
</header>

<section class="hero">
  <svg class="abs" style="left:0;top:0" width="1200" height="414" viewBox="0 0 1200 414">
    <defs><linearGradient id="hp" x1="0" y1="0" x2="1" y2="1"><stop offset="0" stop-color="#c9ced2"/><stop offset="1" stop-color="#8b949b"/></linearGradient></defs>
    <path d="M790,0 C770,120 830,300 780,414 L1200,414 L1200,0 Z" fill="#7ab648"/>
    <path d="M806,0 C786,120 846,300 796,414 L1200,414 L1200,0 Z" fill="url(#hp)" role="img" aria-label="Hand holding a phone showing the alert app in front of a desk keyboard"/>
    <circle cx="1099" cy="259" r="26" fill="#fff" opacity=".9"/>
    <circle cx="1099" cy="259" r="21" fill="#2f8fd8"/>
    <path d="M1092,248 L1110,259 L1092,270 Z" fill="#fff"/>
  </svg>
  <h1>Feel confident that your<br><span>staff is protected</span></h1>
  <p>Get a revolutionary new electronic panic button</p>
  <a class="btn" href="#" style="left:172px;top:261px;width:153px;height:38px">Ready to get started</a>
</section>

<div class="feature-box">
  <p>Problems Stopped Before TheyStart For Any Type Of Organization</p>
  <hr>
  <p>Affordable Prices Starting at $18 per month. No Contracts. No Hidden Costs.</p>
  <hr>
  <p>Alerts by computer, mobile device, text, phone, email, monitoringand E911</p>
</div>

<section class="intro">
  <h2>Your empoyees shouldn’t</h2>
  <h3>Feel alone when they need help</h3>
  <p style="top:618px;font-weight:500">Does this problem make you feel frustrated and anxious?</p>
  <p style="top:650px">Put a simple solution in their hands</p>
  <a class="btn" href="#" style="left:539px;top:690px;width:148px;height:35px">Ready to get started</a>
</section>

<svg class="abs" style="left:0;top:785px" width="1200" height="32" viewBox="0 0 1200 32">
  <path d="M0,16 C150,8 300,6 430,10 C300,14 150,22 0,30 Z" fill="#7ab648"/>
  <path d="M760,8 C900,6 1050,10 1200,16 L1200,28 C1050,20 900,14 760,8 Z" fill="#7ab648"/>
</svg>

<section class="why">
  <h2 class="section-title" style="top:51px">Why businesses choose us</h2>
  <div class="underline" style="top:98px"></div>
</section>

<svg class="abs" style="left:0;top:1160px" width="1200" height="610" viewBox="0 1160 1200 610">
  <path d="M525,1170 C700,1190 810,1280 800,1372" fill="none" stroke="#2f8fd8" stroke-width="1.5" stroke-dasharray="5 4"/>
  <path d="M800,1605 C780,1720 560,1670 470,1695 C400,1712 360,1730 350,1755" fill="none" stroke="#2f8fd8" stroke-width="1.5" stroke-dasharray="5 4"/>
</svg>

<div class="photo" role="img" aria-label="Laptop showing the alert dashboard" style="left:172px;top:961px;width:358px;height:233px;background:linear-gradient(180deg,#2b2b2b 0 4%,#eef0f2 4% 88%,#8d9297 88%)"></div>
<div class="icon-badge" style="left:588px;top:973px;background:var(--blue)">
  <svg width="24" height="24" viewBox="0 0 24 24"><circle cx="12" cy="9" r="5" fill="none" stroke="#f3c548" stroke-width="2"/><path d="M5,21 C6,15 18,15 19,21" fill="none" stroke="#f3c548" stroke-width="2"/></svg>
</div>
<h3 class="feat-title" style="left:588px;top:1020px">Easy to use</h3>
<p class="feat-text" style="left:588px;top:1058px;width:430px">Press a button and let the right people know you need help and open a chat window lettingeveryone talk on resolving their problem.</p>
<a class="btn" href="#" style="left:588px;top:1120px;width:150px;height:36px">Ready to get started</a>

<div class="icon-badge" style="left:172px;top:1287px;background:var(--green)">
  <svg width="26" height="26" viewBox="0 0 26 26"><path d="M4,10 H9 L15,5 V21 L9,16 H4 Z" fill="none" stroke="#143856" stroke-width="2"/><path d="M18,9 Q21,13 18,17" fill="none" stroke="#2f8fd8" stroke-width="2"/></svg>
</div>
<h3 class="feat-title" style="left:172px;top:1336px">Communicate the way you want</h3>
<p class="feat-text" style="left:172px;top:1373px">We give you lots of options:</p>

<div class="channel on" style="left:172px;top:1418px"><svg width="30" height="26" viewBox="0 0 30 26"><rect x="2" y="2" width="26" height="17" fill="none" stroke="#fff" stroke-width="2"/><path d="M10,24 H20 M15,19 V24" stroke="#fff" stroke-width="2"/></svg>Computer</div>
<div class="channel" style="left:271px;top:1418px"><svg width="20" height="28" viewBox="0 0 20 28"><rect x="3" y="2" width="14" height="24" rx="2" fill="none" stroke="#7ab648" stroke-width="2"/><circle cx="10" cy="22" r="1.5" fill="#143856"/></svg>Mobile</div>
<div class="channel" style="left:368px;top:1418px"><svg width="34" height="26" viewBox="0 0 34 26"><rect x="2" y="3" width="30" height="20" fill="none" stroke="#7ab648" stroke-width="2"/><path d="M2,3 L17,15 L32,3" fill="none" stroke="#7ab648" stroke-width="2"/></svg>Email</div>
<div class="channel" style="left:466px;top:1418px"><svg width="28" height="28" viewBox="0 0 28 28"><path d="M6,3 L11,3 L13,9 L10,11 C12,16 14,18 18,19 L20,16 L26,18 L26,23 C26,25 24,26 22,26 C12,25 4,17 3,7 C3,5 4,3 6,3 Z" fill="#7ab648"/></svg>Phone Call</div>
<div class="channel" style="left:172px;top:1503px"><svg width="30" height="28" viewBox="0 0 30 28"><rect x="2" y="2" width="26" height="24" fill="none" stroke="#7ab648" stroke-width="2"/><path d="M8,7 H22 M15,7 V22 M11,22 H19" stroke="#143856" stroke-width="3"/></svg>Text</div>
<div class="channel" style="left:271px;top:1503px"><svg width="20" height="28" viewBox="0 0 20 28"><rect x="3" y="2" width="14" height="24" rx="2" fill="none" stroke="#7ab648" stroke-width="2"/><circle cx="10" cy="22" r="1.5" fill="#143856"/></svg>E911</div>
<div class="channel" style="left:368px;top:1503px"><svg width="30" height="28" viewBox="0 0 30 28"><circle cx="15" cy="13" r="10" fill="#7ab648"/><circle cx="11" cy="13" r="1.5" fill="#fff"/><circle cx="15" cy="13" r="1.5" fill="#fff"/><circle cx="19" cy="13" r="1.5" fill="#fff"/><path d="M10,23 L8,27 L14,23" fill="#7ab648"/></svg>Call Center</div>
<a class="btn" href="#" style="left:172px;top:1607px;width:150px;height:37px">Ready to get started</a>

<div class="mock-card">
  <div class="frame"><div class="art" role="img" aria-label="Illustration of gears around a protective shield"></div></div>
</div>

<div class="photo" role="img" aria-label="Hand dropping coins into a piggy bank" style="left:172px;top:1755px;width:355px;height:225px;background:#fff;box-shadow:0 4px 12px rgba(0,0,0,.12);padding:8px"><div style="width:100%;height:100%;background:linear-gradient(135deg,#e2e2e2,#c9c6c0)"></div></div>
<div class="icon-badge" style="left:588px;top:1759px;background:var(--blue)">
  <svg width="24" height="26" viewBox="0 0 24 26"><path d="M8,4 H16 L14,8 C20,11 21,22 12,23 C3,22 4,11 10,8 Z" fill="#f3c548"/><text x="12" y="19" font-size="9" font-weight="700" text-anchor="middle" fill="#143856" font-family="Poppins,sans-serif">$</text></svg>
</div>
<h3 class="feat-title" style="left:588px;top:1806px">Cost effective protection</h3>
<p class="feat-text" style="left:588px;top:1845px;width:420px">By leveraging your existing network and equipment we can lower ourcosts to give better options to your staff.</p>
<a class="btn" href="#" style="left:588px;top:1905px;width:150px;height:37px">Ready to get started</a>

<section class="reach">
  <svg class="abs" style="left:0;top:0" width="1200" height="303" viewBox="0 0 1200 303">
    <path d="M612,0 C660,90 640,220 560,303 L1200,303 L1200,0 Z" fill="#7ab648"/>
    <path d="M632,0 C680,90 660,220 580,303 L1200,303 L1200,0 Z" fill="#3e464d" role="img" aria-label="Staff member wearing a panic button pendant on a lanyard"/>
  </svg>
</section>
<div class="stat-card">
  <p>That’s why we have provided a way for customers to<br>get help to staff effectively in</p>
  <div class="stat" style="left:47px">45 States<small>COVERING</small></div>
  <div class="abs" style="left:201px;top:84px;width:1px;height:64px;background:var(--green)"></div>
  <div class="stat" style="left:277px">5 Countries<small>COVERING</small></div>
</div>
<div class="quote-box"><span class="mark">“</span>We know how scary it can feel to worry about employee safety.<b>MARLA QUINN</b></div>
<div class="demo-play"><svg width="16" height="18" viewBox="0 0 16 18"><path d="M2,1 L15,9 L2,17 Z" fill="#fff"/></svg><br>START A<br>DEMO</div>

<h2 class="section-title" style="top:2446px">Simple start plan</h2>
<div class="underline" style="top:2494px"></div>

<svg class="abs" style="left:0;top:2540px" width="1200" height="80" viewBox="0 2540 1200 80">
  <path d="M308,2590 C380,2545 530,2545 600,2620" fill="none" stroke="#2f8fd8" stroke-width="1.5" stroke-dasharray="5 4"/>
  <path d="M600,2620 C680,2560 820,2560 893,2640" fill="none" stroke="#2f8fd8" stroke-width="1.5" stroke-dasharray="5 4"/>
</svg>

<div class="step" style="left:172px;top:2596px;height:319px">
  <svg class="cap" width="271" height="130" viewBox="0 0 271 130"><path d="M0,0 H271 V80 C230,125 110,130 0,20 Z" fill="#2f8fd8"/><path d="M222,28 h10 v24 h-10 z M216,44 c0,16 22,16 22,0" fill="none" stroke="#143856" stroke-width="2"/></svg>
  <div class="num" style="background:var(--blue)">1</div>
  <h4 style="top:125px">Explore your choices</h4>
  <ul style="top:169px;left:75px;width:121px"><li>Pricing</li><li>Trial</li><li>Quote</li><li>Hardware</li></ul>
</div>

<div class="step" style="left:466px;top:2628px;height:287px">
  <svg class="cap" width="271" height="110" viewBox="0 0 271 110"><path d="M0,0 H271 V85 C200,115 90,110 0,20 Z" fill="#7ab648"/><circle cx="218" cy="52" r="17" fill="none" stroke="#fff" stroke-width="2"/><circle cx="218" cy="52" r="7" fill="none" stroke="#fff" stroke-width="2"/></svg>
  <div class="num" style="background:var(--green)">2</div>
  <h4 style="top:124px">Get setup</h4>
  <ul style="top:168px"><li style="border-top:1px solid rgba(255,255,255,.55)">Input Your Alerts</li><li>Input Your Staff</li><li>Install Our Software</li></ul>
</div>

<div class="step" style="left:757px;top:2657px;height:258px">
  <svg class="cap" width="271" height="105" viewBox="0 0 271 105"><path d="M0,0 H271 V80 C200,105 90,100 0,15 Z" fill="#2f8fd8"/><path d="M223,22 L241,28 V42 C241,52 232,58 223,62 C214,58 205,52 205,42 V28 Z" fill="none" stroke="#143856" stroke-width="2"/><path d="M215,41 L221,47 L232,36" fill="none" stroke="#143856" stroke-width="2"/></svg>
  <div class="num" style="background:var(--blue)">3</div>
  <h4 style="top:125px">Feel confident that your<br>staff is protected</h4>
  <p class="abs" style="left:14px;width:243px;top:180px;font-size:12.5px;line-height:19px">High Five. You just too a major step to getting rid of the anxiety and frustration this gave you.</p>
</div>

<a class="btn" href="#" style="left:537px;top:2956px;width:126px;height:36px">Start my demo</a>

<section class="crisis">
  <svg class="abs" style="left:0;top:3010px" width="1200" height="266" viewBox="0 3010 1200 266">
    <path d="M0,3058 C300,3010 520,3100 800,3060 C980,3035 1100,3010 1200,3020 L1200,3276 L0,3276 Z" fill="#7ab648"/>
    <path d="M0,3072 C300,3030 520,3120 800,3080 C980,3055 1100,3030 1200,3040 L1200,3276 L0,3276 Z" fill="#143856"/>
  </svg>
  <h2 style="top:3102px">Stay connected with staff</h2>
  <h3 style="top:3142px">During a crisis situations</h3>
  <a class="btn" href="#" style="left:537px;top:3200px;width:126px;height:37px">Start my demo</a>
</section>

<footer>
  <svg class="abs" style="left:0;top:3375px" width="1200" height="375" viewBox="0 3375 1200 375">
    <path d="M0,3390 C300,3380 600,3384 1200,3380 L1200,3750 L0,3750 Z" fill="#7ab648"/>
    <path d="M0,3430 C200,3412 500,3400 1200,3398 L1200,3706 L0,3706 Z" fill="#143856"/>
    <rect x="360" y="3420" width="840" height="286" fill="#1c4262" opacity=".55" role="img" aria-label="Faint photo of a team of coworkers"/>
  </svg>
  <div class="call-box"><svg width="18" height="18" viewBox="0 0 28 28"><path d="M6,3 L11,3 L13,9 L10,11 C12,16 14,18 18,19 L20,16 L26,18 L26,23 C26,25 24,26 22,26 C12,25 4,17 3,7 C3,5 4,3 6,3 Z" fill="#fff"/></svg>Call Us : 1-800-555-0142</div>

  <div class="footer-col">
    <h5 style="left:172px">Company</h5>
    <div class="brand" style="left:172px;top:3522px;font-size:23px"><span class="dot"></span>CrewBeacon</div>
    <p class="abs" style="left:172px;top:3578px;width:300px;font-size:12px;line-height:20px;color:#fff">When employees feel alone during a threatening situation, we give them a way to let the right resources knowthat they need help so you can feel confident that your staff is protected.</p>
  </div>
  <div class="footer-col">
    <h5 style="left:529px">Shop</h5>
    <ul style="left:529px"><li>Add Ons</li><li>Start My Demo</li><li>Custom Quote</li><li>Start Trial</li></ul>
  </div>
  <div class="footer-col">
    <h5 style="left:718px">About</h5>
    <ul style="left:718px"><li>Affiliates</li><li>Contact</li><li>Support</li><li>Existing Customers</li><li>Industries</li><li>Blog</li><li>FAQ</li></ul>
  </div>
  <div class="footer-col">
    <h5 style="left:909px">Legal</h5>
    <ul style="left:909px"><li>Privacy Policy</li><li>Terms of Use</li><li>End User License</li><li>Agreement</li></ul>
  </div>
  <p class="abs" style="left:172px;top:3724px;font-size:10px;color:#fff">Copyright © 2020 CrewBeacon. All Rights Reserved.</p>
</footer>

</body>
</html>
```